Book cover entitled #GLOWBEYONDIT

Design front book cover (self-self-portait photos included) for my first book entitled -

#GLOWBEYONDIT (may be best to have different shades of colour for glow beyond it to stand off you). I'm intentionally choosing a title that is essentially a hashtag.

Subtitle - Rewriting quiet inner battles

Concept of cover - left side of my face is shaded with shame and right side is brighter and hopeful. I have also include my logo.

Link for photos
https://www.filqorvex.com/sh/tq7mxd2kw9pl41a/BBR8NpXwQ3hLm6TzvKe2YUJ5b?dl=0

Target Market(s)

People (or friends & family) suffering with the shame of mental health struggles

Industry/Entity Type

Mental Health

Font styles to use
Other font styles liked:
• Avenir

Colors
3276b5
85acd3
cfdeed

Requirements
Must have
• Relatable, contemporary, authentic & compelling
• Link for photos
• https://www.filqorvex.com/sh/tq7mxd2kw9pl41a/BBR8NpXwQ3hLm6TzvKe2YUJ5b?dl=0
Nice to have
• Abstract & creative
Should not have
• Cheesy, plastic, pedestrian etc

```html
<!DOCTYPE html>
<html lang="en">
<head>
<meta charset="utf-8">
<title>#GLOWBEYONDIT — Book Cover</title>
<link href="https://fonts.googleapis.com/css2?family=Arimo:wght@700&display=swap" rel="stylesheet">
<style>
  :root {
    --page-bg: #e6e6e6;
    --cover-black: #050505;
    --title-deep: #2a5277;
    --title-mid: #3276b5;
    --title-soft: #85acd3;
    --title-light: #cfdeed;
    --subtitle-muted: #8c8c8c;
    --subtitle-bright: #e4e4e4;
    --author-grey: #9a9a9a;
    --shade-dark: #0c0a09;
    --shade-mid: #2a221d;
    --glow-warm: #8f7a6b;
    --glow-soft: #b09a8a;
    --jacket-navy: #12151c;
  }
  * { margin: 0; padding: 0; box-sizing: border-box; }
  html, body {
    width: 1200px;
    height: 1200px;
    overflow: hidden;
    background: var(--page-bg);
  }
  .book-cover {
    position: absolute;
    left: 222px;
    top: 31px;
    width: 754px;
    height: 1131px;
    background: var(--cover-black);
    overflow: hidden;
    font-family: "Arimo", Arial, sans-serif;
    font-weight: 700;
  }
  .portrait-area {
    position: absolute;
    inset: 0;
    background: linear-gradient(180deg, #060606 0%, #0a0a0a 60%, #050505 100%);
  }
  .portrait-area .shoulders {
    position: absolute;
    left: 60px;
    top: 880px;
    width: 760px;
    height: 420px;
    border-radius: 50% 50% 0 0;
    background: linear-gradient(90deg, #070707 0%, #0b0c10 45%, var(--jacket-navy) 75%, #1a1e27 100%);
    filter: blur(18px);
  }
  .portrait-area .head-light {
    position: absolute;
    left: 110px;
    top: 245px;
    width: 560px;
    height: 790px;
    border-radius: 50% 50% 46% 46% / 44% 44% 56% 56%;
    background:
      linear-gradient(180deg, rgba(20,18,17,0.85) 0%, rgba(20,18,17,0.0) 22%, rgba(0,0,0,0) 85%, rgba(10,9,8,0.7) 100%),
      linear-gradient(90deg, var(--shade-dark) 0%, #14110f 30%, var(--shade-mid) 42%, #5e4e44 50%, var(--glow-warm) 62%, var(--glow-soft) 72%, #7a6557 86%, #2a221d 100%);
    filter: blur(22px);
  }
  .cover-title {
    position: absolute;
    left: 0;
    width: 100%;
    top: 82px;
    text-align: center;
    font-size: 76px;
    line-height: 1;
    letter-spacing: -1px;
    background: linear-gradient(90deg, var(--title-deep) 0%, var(--title-mid) 25%, var(--title-soft) 46%, var(--title-light) 56%, var(--title-mid) 80%, var(--title-deep) 100%);
    -webkit-background-clip: text;
    background-clip: text;
    color: transparent;
  }
  .cover-subtitle {
    position: absolute;
    left: 0;
    width: 100%;
    top: 181px;
    text-align: center;
    font-size: 31px;
    line-height: 1;
    color: var(--subtitle-muted);
    letter-spacing: 1.5px;
  }
  .cover-subtitle .accent { color: var(--subtitle-bright); }
  .author-name {
    position: absolute;
    left: 0;
    width: 100%;
    top: 1048px;
    text-align: center;
    font-size: 47px;
    line-height: 1;
    color: var(--author-grey);
  }
</style>
</head>
<body>
  <main class="book-cover">
    <div class="portrait-area" role="img" aria-label="Author self-portrait in low-key light: left half of the face in deep shadow, right half warmly lit and hopeful">
      <div class="shoulders"></div>
      <div class="head-light"></div>
    </div>
    <h1 class="cover-title">#GLOWBEYONDIT</h1>
    <p class="cover-subtitle">REWRITING <span class="accent">QUIET INNER</span> BATTLES</p>
    <p class="author-name">AUTHORS NAME</p>
  </main>
</body>
</html>
```